Client website

Our designer we were working with had some personal things come up and was unable to finish the design for the site.

We have a .psd file started, and will be attaching it to the project.

Reason: I still want to polish the designs with the current designer and allow more designers the opportunity to participate.

Reason: I'm extending the deadline for another day to give everyone enough time for the final changes our client wants.

I'm trying to extend the deadline so we can get one last set of comps in for my client.  Could everyone message me and let me know how much time they need to do the final tweaks?

Reason: Hey everyone.  I've been sick the last 3 days and I haven't been able to provide feedback on designs.  I'm extending just a few more days so I can catch up here.  Thanks everyone for your patience.

Adults in United States aged 25 to 60 that handle the household budgets and maintenance.

• 1) We need 2 pages. 1 page for flood restoration, 1 page for carpet cleaning

2) The 1-800-# must be the focal point of the website for both pages. People are mostly looking to contact someone ASAP to get them out to their house when flooding occurs.

3) We''re going to have a slide show area to high-light different sub-services offered for each page.

4) We really want a pagenest / lumora feed area. We''re going to use pagenest for special offers, and lumora for weather updates. The pagenest feed is going to be on the carpet cleaning page. The lumora feed is going to be on the flood page.

5) We want an SEO text sections near the bottom.

6) The very bottom will link to the privacy policy and user agreement as well as company name and copyright details.

We really want to stick to the say "theme" that our first designer started with.
• I'm not a designer, so if you think something looks better somewhere, or something can be eliminated, or something can be enhanced, but all means, let us know.

```html
<!DOCTYPE html>
<html lang="en">
<head>
<meta charset="utf-8">
<title>Pure-Nova Carpet Cleaning</title>
<link rel="stylesheet" href="https://fonts.googleapis.com/css2?family=Open+Sans:wght@400;600&family=Arimo:wght@400&display=swap">
<style>
:root{
  --page-bg:#1e3246;
  --frame:#3fb6f0;
  --blue:#1b8fdc;
  --blue-dark:#0b4fa6;
  --green:#1aa53a;
  --title-blue:#2a8fd0;
  --text:#111;
  --panel-edge:#dcdcdc;
  --wood-a:#a79a8e;
  --wood-b:#c9beb3;
}
*{box-sizing:border-box;margin:0;padding:0}
html,body{width:1200px;height:1169px;overflow:hidden}
body{background:radial-gradient(ellipse at 50% 30%,#2c4560,var(--page-bg) 70%);font-family:"Arimo",Arial,sans-serif;color:var(--text);position:relative}
.site{position:absolute;left:134px;top:0;width:935px;height:1169px;background:var(--frame)}
.callbar{position:absolute;left:5px;top:0;width:925px;height:64px;background:linear-gradient(#43bdf5,#1b8ad6);text-align:center;font-family:"Open Sans",sans-serif;color:#fff;font-size:46px;line-height:62px;letter-spacing:-.5px}
.hero{position:absolute;left:6px;top:69px;width:923px;height:293px;background:linear-gradient(160deg,#b6ab9f 0%,#d9d0c6 45%,#9c9088 100%)}
.hero-glow{position:absolute;left:40px;top:0;width:300px;height:290px;border-radius:50%;background:radial-gradient(circle,rgba(255,255,255,.85),rgba(255,255,255,0) 65%)}
.brand{position:absolute;left:20px;top:212px;font-family:"Open Sans",sans-serif;font-weight:600;color:var(--blue);font-size:44px;line-height:48px;letter-spacing:1px}
.brand small{display:block;font-size:16px;line-height:22px;letter-spacing:2px;margin-left:85px}
.brand-dot{position:absolute;left:95px;top:40px;width:150px;height:150px;border-radius:50%;background:var(--blue)}
.nav{position:absolute;left:6px;top:365px;display:flex;height:34px}
.nav a{display:block;width:146px;margin-right:1px;background:linear-gradient(#5ac3f4,#1d8bd6);color:#fff;text-decoration:none;text-align:center;font-family:"Open Sans",sans-serif;font-size:16px;line-height:36px;letter-spacing:1.5px}
.nav a.active{background:linear-gradient(#25c04a,#0f9a34)}
.promo{position:absolute;left:739px;top:280px;width:200px;height:120px;border-radius:4px;background:linear-gradient(#3ab4f2,#127fd0);color:#fff;font-family:"Open Sans",sans-serif;text-align:center;padding-top:14px;box-shadow:0 2px 4px rgba(0,0,0,.3)}
.promo strong{display:block;font-weight:400;font-size:33px;line-height:40px}
.promo span{display:block;font-size:17px;line-height:22px}
.content{position:absolute;left:6px;top:400px;width:923px;height:621px;background:repeating-linear-gradient(90deg,var(--wood-a) 0 7px,var(--wood-b) 7px 13px,#b3a79b 13px 22px)}
.features{position:absolute;left:23px;top:36px;width:856px;height:214px;background:#fff;border:7px solid var(--panel-edge);border-radius:22px;display:flex;padding:10px 6px 0}
.feature{flex:1;padding:0 8px;position:relative}
.feature+.feature{border-left:1px dotted #bbb}
.feature h3{font-family:"Open Sans",sans-serif;color:var(--green);font-size:18px;font-weight:600;text-align:center;line-height:22px;margin-bottom:8px}
.feature-photo{display:block;height:88px;border:1px solid #ccc;background:radial-gradient(ellipse at 50% 40%,#f6d34a,#e28a12 60%,#7a3a05)}
.feature p{font-size:13.5px;line-height:17px;margin-top:8px;padding-right:4px}
.more{position:absolute;right:12px;bottom:13px;color:var(--green);font-size:13px;text-decoration:underline}
.reflection{position:absolute;left:23px;top:252px;width:856px;height:70px;border-radius:0 0 22px 22px;background:linear-gradient(rgba(255,255,255,.35),rgba(255,255,255,0))}
.box{position:absolute;top:333px;width:276px;height:214px;background:#fff;border:7px solid var(--panel-edge);border-radius:22px;padding:14px 12px}
.box h2{font-family:"Open Sans",sans-serif;font-weight:400;color:var(--title-blue);font-size:23px;line-height:28px;margin-bottom:8px}
.box p{font-size:13.5px;line-height:17px;padding-left:4px}
.box ul{list-style:none;padding-left:2px}
.box li{font-size:13.5px;line-height:24px;display:flex;align-items:center}
.box li::before{content:"";width:10px;height:10px;background:#4bb3ee;margin-right:12px}
.box li span{border-bottom:1px solid #222;line-height:16px;padding-right:6px}
.social{display:flex;gap:8px;margin:2px 0 12px 2px}
.social span{height:34px;padding:0 4px;border-radius:4px;background:linear-gradient(#6cc7f6,#2b8fd6);color:#fff;font-size:11px;line-height:34px}
.footer{position:absolute;left:0;top:1021px;width:935px;height:148px;background:linear-gradient(#2aa3ea,#0b55ad 14px,var(--blue-dark) 30px)}
.footer p{position:absolute;left:26px;top:42px;width:870px;color:#fff;font-size:11.5px;line-height:14.5px;letter-spacing:-.2px}
</style>
</head>
<body>
<div class="site">
  <header class="callbar">Call Today: 1-800-555-0142</header>
  <div class="hero" role="img" aria-label="Photo of a carpet cleaning wand on a beige carpet">
    <div class="hero-glow"></div>
    <div class="brand-dot"></div>
    <div class="brand">PURE-NOVA<small>Carpet Cleaning</small></div>
  </div>
  <nav class="nav">
    <a class="active" href="#">home</a><a href="#">about</a><a href="#">services</a><a href="#">faq</a><a href="#">contact</a>
  </nav>
  <div class="promo"><strong>Aww YEAH!</strong><span>Check out this special</span><span>Promo stuff RIGHT NOW!</span></div>
  <main class="content">
    <section class="features">
      <article class="feature"><h3>About Pure-Nova</h3><span class="feature-photo" role="img" aria-label="Photo of a team at work"></span><p>Lorem ipsum dolor sit amet, consectetur adipisicing elit, sed do eiusmod tempor incididunt ut labore.</p><a class="more" href="#">View More..</a></article>
      <article class="feature"><h3>About Pure-Nova</h3><span class="feature-photo" role="img" aria-label="Photo of a team at work"></span><p>Lorem ipsum dolor sit amet, consectetur adipisicing elit, sed do eiusmod tempor incididunt ut labore.</p><a class="more" href="#">View More..</a></article>
      <article class="feature"><h3>About Pure-Nova</h3><span class="feature-photo" role="img" aria-label="Photo of a team at work"></span><p>Lorem ipsum dolor sit amet, consectetur adipisicing elit, sed do eiusmod tempor incididunt ut labore.</p><a class="more" href="#">View More..</a></article>
    </section>
    <div class="reflection"></div>
    <section class="box" style="left:23px">
      <h2>Who We Are?</h2>
      <p>Lorem ipsum dolor sit amet, consectetur adipisicing elit, sed do eiusmod tempor incididunt ut labore et dolore magna aliqua.</p>
      <p style="margin-top:17px">Ut enim ad minim veniam, quis nostrud exercitation.</p>
    </section>
    <section class="box" style="left:313px">
      <h2>What We Do?</h2>
      <ul>
        <li><span>Lorem ipsum dolor sit amet,</span></li>
        <li><span>consectetur adipisicing elit</span></li>
        <li><span>sed do eiusmod tempor</span></li>
        <li><span>incididunt ut labore et</span></li>
        <li><span>dolore magna aliqua.</span></li>
      </ul>
    </section>
    <section class="box" style="left:603px">
      <h2>Find Us On?</h2>
      <div class="social"><span>pagenest</span><span>lumora</span><span>rss</span><span>stackly</span></div>
      <p>Lorem ipsum dolor sit amet, consectetur adipisicing elit, sed do eiusmod tempor incididunt ut labore et dolore magna aliqua.</p>
    </section>
  </main>
  <footer class="footer">
    <p>Lorem Ipsum is simply dummy text of the printing and typesetting industry. Lorem Ipsum has been the industry's standard dummy text ever since the 1500s, when an unknown printer took a galley of type and scrambled it to make a type specimen book. It has survived not only five centuries, but also the leap into electronic typesetting, remaining essentially unchanged. Lorem Ipsum is simply dummy text of the printing and typesetting industry. Lorem Ipsum has been the industry's standard dummy text ever since the 1500s, when an unknown printer took a galley of type and scrambled it to make a type specimen book. It has survived not only five centuries, but also the leap into electronic typesetting, remaining essentially unchanged.</p>
  </footer>
</div>
</body>
</html>
```